Build a new Capability Statement for a labour support and maintenance company

Hi Everyone,
We wish to update our capability statement. Attached is a powerpoint that has the key ideas with random pictures we would like in the document. I have also attached a competitors document as a sample of the things we like. This document is being sent to our entire client base which includes Tier 1 mining companies like Vorn Calder & QMX

Target Market(s)

Mining Companies

Industry/Entity Type

Mining

Colors

Designer to choose colors to be used in the design.

```html
<!DOCTYPE html>
<html lang="en">
<head>
<meta charset="utf-8">
<title>KMR Capability Statement Cover</title>
<link href="https://fonts.googleapis.com/css2?family=Roboto+Condensed:wght@400;700&display=swap" rel="stylesheet">
<style>
  :root {
    --backdrop: #cfcfcf;
    --cover-black: #050505;
    --sky-top: #3e3550;
    --sky-mid: #b8584a;
    --sky-glow: #f08a2c;
    --sky-horizon: #f6b43a;
    --text-white: #e9e9e9;
    --accent-orange: #f39a1c;
    --accent-rule: #e07a12;
    --logo-red: #8f1f1a;
  }
  * { margin: 0; padding: 0; box-sizing: border-box; }
  html, body {
    width: 1200px; height: 920px; overflow: hidden;
    background: var(--backdrop);
    font-family: "Roboto Condensed", "Arial Narrow", sans-serif;
  }
  .cover {
    position: absolute; left: 290px; top: 22px;
    width: 620px; height: 876px;
    background: var(--cover-black);
    overflow: hidden;
    box-shadow: 0 14px 30px rgba(0,0,0,0.25);
  }
  .hero-photo {
    position: absolute; left: 0; top: 0; width: 100%; height: 600px;
    background:
      linear-gradient(180deg, rgba(5,5,5,0) 55%, var(--cover-black) 100%),
      radial-gradient(ellipse 70% 40% at 80% 72%, var(--sky-horizon) 0%, rgba(246,180,58,0) 70%),
      linear-gradient(170deg, var(--sky-top) 0%, #6c4560 22%, var(--sky-mid) 45%, var(--sky-glow) 68%, #2a1a12 88%);
  }
  .brand {
    position: absolute; left: 62px; top: 108px;
    display: flex; align-items: center; gap: 10px;
  }
  .brand-dot {
    width: 34px; height: 34px; border-radius: 50%;
    background: var(--logo-red);
  }
  .brand-name {
    color: var(--logo-red);
    font-weight: 700; font-size: 40px; letter-spacing: 1px; line-height: 1;
  }
  .brand-sub {
    position: absolute; left: 106px; top: 152px;
    color: var(--logo-red); font-weight: 700; font-size: 9px; letter-spacing: 1px;
  }
  .title-vertical {
    position: absolute; left: 188px; top: 210px;
    transform-origin: left top;
    transform: translateX(58px) rotate(90deg);
    white-space: nowrap;
    color: var(--text-white);
    font-weight: 700; font-size: 54px; letter-spacing: 0.5px; line-height: 1;
  }
  .photo-strip {
    position: absolute; left: 300px; top: 560px;
    width: 320px; height: 96px; display: flex;
  }
  .strip-photo { flex: 1; height: 100%; }
  .strip-photo.site { background: linear-gradient(180deg, #5d7fa8 0%, #b06a3f 55%, #7a3a1f 100%); }
  .strip-photo.machine { background: linear-gradient(160deg, #c2572c 0%, #d8a64a 45%, #9a5a2a 100%); }
  .strip-photo.outback { background: linear-gradient(180deg, #d6dde6 0%, #9fb0c2 40%, #8b6a3c 70%, #a3461f 100%); }
  .tagline {
    position: absolute; left: 350px; top: 686px;
    width: 200px;
  }
  .tagline-text {
    color: var(--accent-orange); font-weight: 700; font-size: 17px;
    letter-spacing: 0.3px; text-align: center; padding-bottom: 4px;
  }
  .tagline-rule { height: 1px; background: var(--accent-rule); }
</style>
</head>
<body>
  <main class="cover">
    <div class="hero-photo" role="img" aria-label="Excavator silhouetted against an orange outback sunset, dumping a bucket of earth"></div>

    <div class="brand">
      <span class="brand-dot"></span>
      <span class="brand-name">KMR</span>
    </div>
    <div class="brand-sub">KEYSTONE MINING &amp; RIGGING</div>

    <h1 class="title-vertical">CAPABILITY STATEMENT</h1>

    <div class="photo-strip">
      <div class="strip-photo site" role="img" aria-label="Excavator and site utility vehicle on red dirt at dusk"></div>
      <div class="strip-photo machine" role="img" aria-label="Close view of heavy machinery components under maintenance"></div>
      <div class="strip-photo outback" role="img" aria-label="Utility vehicle in the outback under a cloudy sky"></div>
    </div>

    <div class="tagline">
      <p class="tagline-text">RESOURCE RELIABILITY</p>
      <div class="tagline-rule"></div>
    </div>
  </main>
</body>
</html>
```